Postcard Design Project

Freight forwarder, Customs Broker, Storage Facility

Target Market(s)

Persons shipping from Florida

Industry/Entity Type

Shipping

Font styles to use
Serif

Colors

Designer to choose colors to be used in the design.

Requirements
Must have
• A boat and plane picture, two-sided cards, Please see sample postcard submitted!!
• 5x7 Flyer
• We would like a front and back design. On the front design we would like to suggest removing the address from the footer. Apply our mission statement, and services (listed as titles only) with logo as silhouette /background. The backside our addresses/contact in vertical alignememt, side by side if possible. This back side can also have our logo center top and ship and air craft mentioned in business card design can be used as a silhouette/ background.

```html
<!DOCTYPE html>
<html lang="en">
<head>
<meta charset="utf-8">
<title>Tidewind Freight – Flyer Front and Back</title>
<link href="https://fonts.googleapis.com/css2?family=PT+Serif:wght@400;700&display=swap" rel="stylesheet">
<style>
  :root{
    --navy:#2a3766;
    --navy-deep:#1f2a52;
    --red:#e21d2a;
    --white:#ffffff;
    --cream:#f6eadf;
    --stage:#ece6dc;
    --sky-top:#6f9fd6;
    --sky-light:#dbe7f2;
    --sea:#3f8fa8;
    --dusk-top:#2b4f8f;
    --dusk-glow:#f3b24a;
  }
  *{box-sizing:border-box;margin:0;padding:0}
  html,body{width:1200px;height:960px;overflow:hidden}
  body{background:var(--stage);font-family:"PT Serif",Georgia,serif;color:var(--white);position:relative}
  .flyer{position:absolute;top:84px;width:510px;height:714px;overflow:hidden;background:var(--navy);box-shadow:0 10px 22px rgba(0,0,0,.25)}
  .flyer--front{left:84px}
  .flyer--back{left:641px}
  .flyer__art{position:absolute;inset:0;width:510px;height:714px;display:block}
  .brand{position:absolute;display:flex;align-items:center;gap:8px;font-weight:700;font-size:21px;letter-spacing:.2px;white-space:nowrap}
  .brand__dot{width:20px;height:20px;border-radius:50%;background:var(--cream);flex:none}
  .flyer--front .brand{left:292px;top:120px;color:var(--navy-deep)}
  .flyer--back .brand{left:152px;top:118px;color:var(--white)}
  .section-title{position:absolute;left:32px;font-weight:700;font-size:24px;letter-spacing:.3px;text-transform:uppercase;white-space:nowrap}
  .mission-title{top:358px}
  .mission-text{position:absolute;left:32px;top:393px;width:452px;font-size:13.6px;line-height:17px}
  .services-title{top:450px}
  .services{position:absolute;left:32px;top:484px;list-style:none;font-size:14.6px;line-height:17.1px;white-space:nowrap}
  .services li{display:flex;align-items:center;gap:12px}
  .services svg{width:13px;height:9px;flex:none}
  .phone{position:absolute;left:28px;top:668px;display:flex;align-items:center;gap:8px;font-size:23px;font-weight:700;white-space:nowrap}
  .phone svg{width:22px;height:22px}
  .about-title{position:absolute;left:29px;top:350px;font-size:19px;font-weight:700}
  .about-text{position:absolute;left:29px;top:379px;width:452px;font-size:13px;line-height:16.6px;text-align:justify}
  .about-text p{margin:0}
  .address{position:absolute;top:618px;font-size:12px;line-height:16px;white-space:nowrap}
  .address--local{left:24px}
  .address--us{left:218px}
  .address__title{font-weight:700;font-size:13px;text-transform:uppercase;margin-left:17px;margin-bottom:1px}
  .address__line{display:flex;align-items:center;gap:6px}
  .address__line svg{width:11px;height:11px;flex:none}
  .address__line .gap{width:11px;flex:none}
  .address__line--phone{margin-top:4px}
</style>
</head>
<body>

<section class="flyer flyer--front">
  <svg class="flyer__art" viewBox="0 0 510 714">
    <defs>
      <linearGradient id="frontSky" x1="0" y1="0" x2="0" y2="1">
        <stop offset="0" stop-color="var(--sky-light)"/>
        <stop offset=".45" stop-color="var(--sky-top)"/>
        <stop offset=".8" stop-color="#e8eef3"/>
        <stop offset="1" stop-color="var(--sea)"/>
      </linearGradient>
      <linearGradient id="frontInset" x1="0" y1="0" x2="0" y2="1">
        <stop offset="0" stop-color="#9cc3e8"/>
        <stop offset=".5" stop-color="#3fa6c4"/>
        <stop offset="1" stop-color="#c79a5a"/>
      </linearGradient>
    </defs>
    <path role="img" aria-label="Photo of a passenger airliner in flight above a large cruise ship at sea" d="M0 0H510V300C380 350 160 362 0 282Z" fill="url(#frontSky)"/>
    <path d="M0 282C160 362 380 350 510 300V306C380 362 160 376 0 298Z" fill="var(--white)"/>
    <path d="M0 298C160 376 380 362 510 306V314C380 382 160 400 0 322Z" fill="var(--red)"/>
    <path d="M0 650C130 636 260 650 320 714" fill="none" stroke="var(--white)" stroke-width="6"/>
    <path d="M0 656C130 642 255 658 312 714H0Z" fill="var(--red)"/>
    <circle role="img" aria-label="Photo of a container ship stacked with cargo on blue water" cx="436" cy="604" r="128" fill="url(#frontInset)" stroke="var(--white)" stroke-width="5"/>
  </svg>

  <div class="brand"><span class="brand__dot"></span>Tidewind Freight</div>

  <h2 class="section-title mission-title">Our Mission:</h2>
  <p class="mission-text">Our mission is constantly esceed customer expectations by providing superior freight forwarding and global tranportation solutions including brokerage and logistics services.</p>

  <h2 class="section-title services-title">Our Services Incude:</h2>
  <ul class="services">
    <li><svg viewBox="0 0 13 9"><path d="M0 4.5H11M7.5 1L11.5 4.5 7.5 8" fill="none" stroke="#fff" stroke-width="1.6"/></svg>Package Deals for Ocean Freight Consumers</li>
    <li><svg viewBox="0 0 13 9"><path d="M0 4.5H11M7.5 1L11.5 4.5 7.5 8" fill="none" stroke="#fff" stroke-width="1.6"/></svg>Customer Online Access</li>
    <li><svg viewBox="0 0 13 9"><path d="M0 4.5H11M7.5 1L11.5 4.5 7.5 8" fill="none" stroke="#fff" stroke-width="1.6"/></svg>U.S. Pick-ups</li>
    <li><svg viewBox="0 0 13 9"><path d="M0 4.5H11M7.5 1L11.5 4.5 7.5 8" fill="none" stroke="#fff" stroke-width="1.6"/></svg>Moving/packing</li>
    <li><svg viewBox="0 0 13 9"><path d="M0 4.5H11M7.5 1L11.5 4.5 7.5 8" fill="none" stroke="#fff" stroke-width="1.6"/></svg>Free Consolidation</li>
    <li><svg viewBox="0 0 13 9"><path d="M0 4.5H11M7.5 1L11.5 4.5 7.5 8" fill="none" stroke="#fff" stroke-width="1.6"/></svg>In-House Brokerage Services</li>
    <li><svg viewBox="0 0 13 9"><path d="M0 4.5H11M7.5 1L11.5 4.5 7.5 8" fill="none" stroke="#fff" stroke-width="1.6"/></svg>Delivery/ Handling</li>
    <li><svg viewBox="0 0 13 9"><path d="M0 4.5H11M7.5 1L11.5 4.5 7.5 8" fill="none" stroke="#fff" stroke-width="1.6"/></svg>Domestic Shipping Services</li>
    <li><svg viewBox="0 0 13 9"><path d="M0 4.5H11M7.5 1L11.5 4.5 7.5 8" fill="none" stroke="#fff" stroke-width="1.6"/></svg>Eaport Services</li>
  </ul>

  <div class="phone">
    <svg viewBox="0 0 24 24"><circle cx="12" cy="12" r="10.5" fill="none" stroke="#fff" stroke-width="2"/><path d="M8.2 6.5l2 2.2-1.1 1.5c.8 1.7 2 2.9 3.7 3.7l1.5-1.1 2.2 2-1.2 1.8c-3.9-.5-7.2-3.8-7.7-7.7z" fill="#fff"/></svg>
    (242) 555-0148
  </div>
</section>

<section class="flyer flyer--back">
  <svg class="flyer__art" viewBox="0 0 510 714">
    <defs>
      <linearGradient id="backSky" x1="0" y1="0" x2="0" y2="1">
        <stop offset="0" stop-color="var(--dusk-top)"/>
        <stop offset=".5" stop-color="#7f8fb0"/>
        <stop offset=".72" stop-color="var(--dusk-glow)"/>
        <stop offset="1" stop-color="#4d5f7a"/>
      </linearGradient>
    </defs>
    <path role="img" aria-label="Photo of a loaded container ship at sea under a sunset sky" d="M0 0H510V300C380 350 160 362 0 282Z" fill="url(#backSky)"/>
    <path d="M0 282C160 362 380 350 510 300V306C380 362 160 376 0 298Z" fill="var(--white)"/>
    <path d="M0 298C160 376 380 362 510 306V314C380 382 160 400 0 322Z" fill="var(--red)"/>
    <path d="M0 600C140 568 330 572 510 690" fill="none" stroke="var(--white)" stroke-width="6"/>
    <path d="M0 606C140 574 330 580 510 698V714H0Z" fill="var(--red)"/>
  </svg>

  <div class="brand"><span class="brand__dot"></span>Tidewind Freight</div>

  <h2 class="about-title">Lorem Ipsum</h2>
  <div class="about-text">
    <p>Lorem Ipsum is simply dummy text of the printing and typesetting industry. Lorem Ipsum has been the industry's standard dummy text ever since the 1500s, when an unknown printer took a galley of type and scrambled it to make a type specimen book. It has survived not only five centuries, but also the leap into electronic typesetting, remaining essentially unchanged. It was popularised in the 1960s with the release of Typemark sheets containing Lorem Ipsum passages, and more recently with desktop publishing software like Pagecraft Studio including versions of Lorem Ipsum.</p>
    <p>Contrary to popular belief, Lorem Ipsum is not simply random text. It has roots in a piece of classical Latin literature from 45 BC, making it over 2000 years old.</p>
  </div>

  <div class="address address--local">
    <div class="address__title">Local Agent Address</div>
    <div class="address__line"><svg viewBox="0 0 12 12"><path d="M6 11S2 7 2 4.5a4 4 0 018 0C10 7 6 11 6 11z" fill="none" stroke="#fff"/><circle cx="6" cy="4.5" r="1.4" fill="#fff"/></svg>48 Harbour View Lane</div>
    <div class="address__line"><span class="gap"></span>P.O. Box SP-20417</div>
    <div class="address__line"><span class="gap"></span>Nassau, N.P. Bahamas</div>
    <div class="address__line address__line--phone"><svg viewBox="0 0 24 24"><circle cx="12" cy="12" r="10.5" fill="none" stroke="#fff" stroke-width="2"/><path d="M8.2 6.5l2 2.2-1.1 1.5c.8 1.7 2 2.9 3.7 3.7l1.5-1.1 2.2 2-1.2 1.8c-3.9-.5-7.2-3.8-7.7-7.7z" fill="#fff"/></svg>(242) 555-0148</div>
  </div>

  <div class="address address--us">
    <div class="address__title">U.S. Address</div>
    <div class="address__line"><svg viewBox="0 0 12 12"><path d="M6 11S2 7 2 4.5a4 4 0 018 0C10 7 6 11 6 11z" fill="none" stroke="#fff"/><circle cx="6" cy="4.5" r="1.4" fill="#fff"/></svg>Tidewind Freight Ltd.</div>
    <div class="address__line"><span class="gap"></span>2710 NW 74th Street</div>
    <div class="address__line"><span class="gap"></span>Miami, FL 33166</div>
    <div class="address__line address__line--phone"><svg viewBox="0 0 24 24"><circle cx="12" cy="12" r="10.5" fill="none" stroke="#fff" stroke-width="2"/><path d="M8.2 6.5l2 2.2-1.1 1.5c.8 1.7 2 2.9 3.7 3.7l1.5-1.1 2.2 2-1.2 1.8c-3.9-.5-7.2-3.8-7.7-7.7z" fill="#fff"/></svg>1-(305)-555-0193</div>
  </div>
</section>

</body>
</html>
```